July 2022 Industrial Manufacturer Product Expo Mexico City

We manufacture large screws and fastners for large Mining equipment, Trains, large ships, airplanes, wind turbines, and so on. We also do custom work base on the customer needs. No matter the size we can make it.
We have a Expo coming up with companies all over the world. We have to stand out we are a family own business so our customer service will be above and beyond anyone can provide. We do not have a sales force to push our products and services we provide one on one service.
Plus@!! I'm looking for anything that you designers can come up with if it was your company to put on a business card, plus i want to do a 1 or 2 sided pamphlet, and then a website. We make Speciality Bolts for large mining equipment these bolts can be 3 to 4 foot long!!! Plus fasteners, Nuts, washers, any, size, strengths, special materials, we offer more of a ono on one customer service, We are a small company, family own, but can fulfill any type of orders. We can also provide special time lines for emergency orders. "We keep the machines running we here at KRV don't believe in down time" We want to hear any slogan based on our company to stand out.
Thanks i really appreciate all your work and options that we have to pick on. Plus just a thought we could possibly want to entertain a experience Marketing internet help maybe a employment possibility. Thanks
Updates

I need 2 cards one in Spanish and English Like the steel back ground maybe send me in some bright red and blue writing Same with the Black cards Please remove the word Military The logo KRV maybe integrate a picture of a Bolt 🔩 Thank you

Still looking for I need 2 cards one in Spanish and English Like the steel back ground maybe send me in some bright red and blue writing Same with the Black cards try bright writing Please remove the word Military The logo KRV maybe integrate a picture of a Bolt 🔩 Plus will need the company to make a brochure and website next Thank you

Target Market(s)

Large Mining, Ship, Train, Green Energy, ORBA, and Government equipment. Throughout the World

Industry/Entity Type

We can Custom Manufacture any type of Fastners for Mining equipment, Trains, Ships, Green energy, Governments, or military projects. wind turbines,

Contact Information for Business Card

I attached the name and contact info that's on a card, plus the Company Logo. Would like industrial looking background with Bright Colors that will stand out!! If we can insert somewhere maybe on back that we "Custom Manufacture Any Size or Quantity Fastners for Large Mining Equipment, Trains, Ships, Green Energy Equipment or Government Projects

Font styles to use
Other font styles liked:
• You Pick, has to be bold, colorful standout, Professional looking Beable to read it.

Colors

Designer to choose colors to be used in the design.

Requirements
Must have
• Need in Spanish and English TO STANDOUT FROM THE REST OF THE EXPO!! See Business card details, Rounded corners
Nice to have
• Can i see some of the darker cards with Bright Red and Blue letters I like to see the different type of card material, heavy thickness, plastic, transparent, Metal types, Bright Colors, I saw like Raised letters like on the logo.

```html
<!DOCTYPE html>
<html lang="en">
<head>
<meta charset="utf-8">
<title>KRV Business Cards</title>
<link href="https://fonts.googleapis.com/css2?family=Lato:wght@400;700;900&display=swap" rel="stylesheet">
<style>
  :root {
    --backdrop: #d3d3ce;
    --card-white: #ffffff;
    --card-black: #080808;
    --brand-blue: #1a8fd6;
    --brand-grey: #4a4a4c;
    --text-dark: #333333;
    --text-light: #f2f2f2;
    --text-light-alt: #9fd2f2;
    --rule: #9a9a9a;
  }
  * { margin: 0; padding: 0; box-sizing: border-box; }
  html, body { width: 1200px; height: 801px; overflow: hidden; }
  body {
    background: var(--backdrop);
    font-family: 'Lato', sans-serif;
    position: relative;
  }
  .card {
    position: absolute;
    top: 246px;
    width: 540px;
    height: 309px;
    border-radius: 10px;
    overflow: hidden;
  }
  .card-front { left: 40px; background: var(--card-white); }
  .card-back { left: 620px; background: var(--card-black); }

  .wordmark {
    position: absolute;
    left: 0; right: 0;
    text-align: center;
    font-weight: 900;
    letter-spacing: 6px;
    line-height: 1;
  }
  .card-front .wordmark {
    top: 46px;
    font-size: 92px;
    color: var(--brand-grey);
  }
  .card-back .wordmark {
    top: 40px;
    font-size: 88px;
    color: var(--brand-blue);
  }

  .person {
    position: absolute;
    left: 30px; bottom: 42px;
    width: 222px;
  }
  .person-name {
    font-size: 22px;
    font-weight: 700;
    color: var(--brand-blue);
    white-space: nowrap;
  }
  .person-title {
    font-size: 14px;
    color: var(--text-dark);
    text-align: right;
    margin-top: 2px;
    white-space: nowrap;
  }
  .divider {
    position: absolute;
    left: 262px; bottom: 34px;
    width: 1px; height: 76px;
    background: var(--rule);
  }
  .contacts {
    position: absolute;
    left: 280px; bottom: 30px;
    list-style: none;
  }
  .contacts li {
    display: flex;
    align-items: center;
    gap: 8px;
    font-size: 12.5px;
    color: var(--text-dark);
    line-height: 20px;
    white-space: nowrap;
  }
  .contacts svg { width: 13px; height: 13px; flex: none; }

  .services {
    position: absolute;
    left: 0; right: 0;
    text-align: center;
    font-size: 14px;
    line-height: 21px;
    white-space: nowrap;
  }
  .services-en { bottom: 88px; color: var(--text-light); }
  .services-es { bottom: 34px; color: var(--text-light-alt); }
</style>
</head>
<body>
  <section class="card card-front">
    <div class="wordmark">KRV</div>
    <div class="person">
      <div class="person-name">Lic Marisol Venegas</div>
      <div class="person-title">President · Presidente</div>
    </div>
    <div class="divider"></div>
    <ul class="contacts">
      <li>
        <svg viewBox="0 0 16 16"><path fill="var(--brand-blue)" d="M2 5c0-2 2-3 6-3s6 1 6 3v1h-3V5H5v1H2zM3 7h10l1 7H2z"/><circle cx="8" cy="10.5" r="2" fill="#fff"/></svg>
        555 204 3187
      </li>
      <li>
        <svg viewBox="0 0 16 16"><rect x="4" y="1" width="8" height="14" rx="1.5" fill="none" stroke="var(--brand-blue)" stroke-width="1.6"/><circle cx="8" cy="12.5" r="0.9" fill="var(--brand-blue)"/></svg>
        555 610 7249
      </li>
      <li>
        <svg viewBox="0 0 16 16"><rect x="1" y="3" width="14" height="10" fill="var(--brand-blue)"/><path d="M1 3l7 6 7-6" fill="none" stroke="#fff" stroke-width="1.2"/></svg>
        tornilleriakrv.ventas@correo.com
      </li>
      <li>
        <svg viewBox="0 0 16 16"><circle cx="8" cy="8" r="6.5" fill="none" stroke="var(--brand-blue)" stroke-width="1.4"/><ellipse cx="8" cy="8" rx="2.8" ry="6.5" fill="none" stroke="var(--brand-blue)" stroke-width="1"/><path d="M1.5 8h13M3 4.5h10M3 11.5h10" stroke="var(--brand-blue)" stroke-width="1"/></svg>
        www.krvcotizaciones.mx
      </li>
    </ul>
  </section>

  <section class="card card-back">
    <div class="wordmark">KRV</div>
    <p class="services services-en" lang="en">
      Custom Manufacture&nbsp; || &nbsp;Large Mining Equipment&nbsp; || &nbsp;Trains<br>
      Ships&nbsp; || &nbsp;Green Energy Equipment&nbsp; || &nbsp;Government Projects
    </p>
    <p class="services services-es" lang="es">
      Fabricación a Medida&nbsp; || &nbsp;Equipo Minero Pesado&nbsp; || &nbsp;Trenes<br>
      Barcos&nbsp; || &nbsp;Equipo de Energía Verde&nbsp; || &nbsp;Proyectos de Gobierno
    </p>
  </section>
</body>
</html>
```